Business card for law firm

Need business card for new law firm. Think confident, authoritative, conservative, but not stuffy or old-fashioned.

Contact Information for Business Card

Content for card - logo (uploaded), plus the following:

Paul Wexbury (larger font)
Managing Partner (larger font, but not as large as name)
Level 9, 41 Tansy Lane
Sydney NSW 2000
Main Tel 02 7346 2190
Direct Tel 02 6273 4415
Email paul@qvlegal.com.au
www.qvlegal.com.au

Letterhead design should include logo plus:
Level 9, 41 Tansy Lane
Sydney NSW 2000
Tel 02 6273 4415
www.qvlegal.com.au

```html
<!DOCTYPE html>
<html lang="en">
<head>
<meta charset="utf-8">
<title>Quillvale Legal — Business Card</title>
<link rel="stylesheet" href="https://fonts.googleapis.com/css2?family=Cinzel:wght@400;500;600&display=swap">
<style>
  :root {
    --bg: #e6e7ea;
    --card: #ffffff;
    --card-shade: #eeeff1;
    --navy: #1f3a78;
    --ink: #1c1c1e;
    --shadow: rgba(40, 44, 52, 0.18);
  }
  * { box-sizing: border-box; margin: 0; padding: 0; }
  html, body {
    width: 1200px;
    height: 800px;
    overflow: hidden;
    background: var(--bg);
  }
  .canvas {
    position: relative;
    width: 1200px;
    height: 800px;
    display: flex;
    align-items: center;
    justify-content: center;
  }
  .business-card {
    position: relative;
    width: 1000px;
    height: 610px;
    background: var(--card);
    box-shadow: 0 18px 40px var(--shadow), 0 2px 6px var(--shadow);
    overflow: hidden;
    font-family: "Cinzel", "Times New Roman", serif;
  }
  .card-texture {
    position: absolute;
    inset: 0;
    background: linear-gradient(160deg, var(--card) 30%, var(--card-shade) 100%);
  }
  .contact-block {
    position: absolute;
    left: 110px;
    top: 190px;
  }
  .contact-name {
    color: var(--navy);
    font-size: 40px;
    font-weight: 500;
    letter-spacing: 0.5px;
    line-height: 1.1;
  }
  .contact-title {
    display: inline-block;
    color: var(--ink);
    font-size: 28px;
    font-weight: 500;
    border-bottom: 2px solid var(--ink);
    line-height: 1.15;
    margin-bottom: 22px;
  }
  .contact-details {
    list-style: none;
    font-size: 21px;
    line-height: 1.3;
    color: var(--ink);
  }
  .contact-details .is-link { color: var(--navy); }
  .brand {
    position: absolute;
    left: 610px;
    top: 260px;
    display: flex;
    align-items: center;
    gap: 22px;
  }
  .brand-square {
    width: 58px;
    height: 58px;
    background: var(--navy);
  }
  .brand-name {
    color: var(--ink);
    font-size: 40px;
    font-weight: 500;
    line-height: 1.05;
    letter-spacing: 2px;
  }
</style>
</head>
<body>
  <main class="canvas">
    <article class="business-card">
      <div class="card-texture" role="img" aria-label="Fine diagonal pinstripe texture across the card in pale grey"></div>

      <section class="contact-block">
        <h1 class="contact-name">Paul Wexbury</h1>
        <p class="contact-title">Managing Partner</p>
        <ul class="contact-details">
          <li>Level 9, 41 Tansy Lane</li>
          <li>Sydney NSW 2000</li>
          <li>Main Tel: 02 7346 2190</li>
          <li>Direct Tel: 02 6273 4415</li>
          <li class="is-link">Email: paul@qvlegal.com.au</li>
          <li class="is-link">www.qvlegal.com.au</li>
        </ul>
      </section>

      <div class="brand">
        <span class="brand-square" aria-hidden="true"></span>
        <p class="brand-name">Quillvale<br>Legal</p>
      </div>
    </article>
  </main>
</body>
</html>
```